Master slides for standard ppt presentation

I just my company, went through GlyphMeadow for the log design and already have an identity that I like.
I need to transpose this identity into some nice Master slides for Powerpoint presentation. I want it clean, with fresh color connection to my logo, not over crowded and obviously different vs what powerpoint proposes as standard design ideas. I will attach a few materials that I already use, branded with the company logo so that you can take inspiration.

```html
<!DOCTYPE html>
<html lang="en">
<head>
<meta charset="utf-8">
<title>Valoreon – Master Slides</title>
<link href="https://fonts.googleapis.com/css2?family=Barlow:wght@500;600;700&family=Montserrat:wght@400;500&display=swap" rel="stylesheet">
<style>
:root{
  --page:#159e86;
  --deep:#0a5345;
  --brand:#1fc88b;
  --bright:#22e69a;
  --teal:#2ab3a2;
  --ink:#2a2f2e;
  --muted:#5d6664;
  --paper:#ffffff;
  --mist:#eef3f2;
  --line:#3fbfa3;
}
*{margin:0;padding:0;box-sizing:border-box}
html,body{width:1200px;height:4147px;overflow:hidden}
body{background:var(--page);position:relative;font-family:"Montserrat",sans-serif;color:var(--ink)}
.slide{position:absolute;left:43px;width:1112px;height:625px;background:linear-gradient(135deg,#ffffff 0%,var(--mist) 100%);overflow:hidden}
.s1{top:55px}.s2{top:733px}.s3{top:1413px}.s4{top:2091px}.s5{top:2771px}.s6{top:3450px}
.abs{position:absolute}
.wordmark{display:flex;align-items:center;gap:10px;font-family:"Barlow",sans-serif;font-weight:700;color:var(--deep);letter-spacing:.5px}
.wordmark .dot{background:var(--brand);border-radius:50%}
.wordmark.large{font-size:26px}.wordmark.large .dot{width:30px;height:30px}
.wordmark.small{font-size:15px}.wordmark.small .dot{width:16px;height:16px}
.corner-mark{right:22px;top:30px}
.title{font-family:"Barlow",sans-serif;font-weight:600;color:var(--brand);line-height:1;letter-spacing:.5px}
.slide-title{font-size:54px;left:34px;top:27px}
.hero-title{font-size:56px;line-height:1.2}
.date{font-size:16px;color:var(--muted);display:flex;align-items:center;gap:12px}
.photo{background:linear-gradient(160deg,#8a9aa3,#3d4a52 60%,#6b5a4c)}
/* agenda */
.agenda-photo{left:0;top:47px;width:435px;height:578px;border-top-right-radius:18px}
.agenda-frame{left:-10px;top:34px;width:462px;height:620px;border:1.5px solid var(--line);border-radius:18px}
.agenda-title{left:670px;top:98px;font-size:54px}
.agenda-list{left:670px;top:190px;list-style:none}
.agenda-list li{display:flex;align-items:center;gap:22px;height:63px;font-size:20px;color:var(--ink)}
.num{width:36px;height:36px;border-radius:50%;background:var(--deep);color:#fff;font-size:14px;display:flex;align-items:center;justify-content:center;box-shadow:0 0 0 4px #c9ece2}
.soft-circle{left:932px;top:317px;width:130px;height:130px;border-radius:50%;background:#e9eeed}
/* capability */
.body-copy{font-size:17px;line-height:33px;color:var(--ink);text-align:justify}
.cap-copy{left:35px;top:146px;width:581px}
.cap-copy p+p{margin-top:12px}
.cap-frame{left:678px;top:128px;width:460px;height:520px;border-top:1.5px solid var(--line);border-left:1.5px solid var(--line);border-top-left-radius:18px}
.cap-photo{left:661px;top:138px;width:451px;height:487px;border-top-left-radius:18px;background:linear-gradient(170deg,#f0d9c4,#3a4a6a 45%,#8a6a4a 100%)}
/* services */
.intro{left:35px;top:117px;width:1045px;font-size:17px;line-height:33px}
.service{top:253px;width:314px;text-align:center}
.service .ring{width:120px;height:120px;border-radius:50%;margin:0 auto;display:flex;align-items:center;justify-content:center;background:#c9ece6}
.service .core{width:96px;height:96px;border-radius:50%;display:flex;align-items:center;justify-content:center}
.service h3{font-family:"Barlow",sans-serif;font-weight:600;font-size:17px;margin-top:24px;letter-spacing:.3px}
.service p{font-size:13.5px;line-height:26px;color:var(--muted);margin-top:8px;text-align:justify;text-align-last:center}
/* testimonial */
.bubble{width:332px;height:332px;border-radius:50%;background:#fff;box-shadow:0 10px 30px rgba(0,0,0,.08);text-align:center}
.avatar{position:absolute;left:50%;width:104px;height:104px;margin-left:-52px;border-radius:50%;border:3px solid #fff;box-shadow:0 0 0 2px var(--line);background:linear-gradient(180deg,#c7ced0,#3f4a55)}
.bubble h3{font-family:"Barlow",sans-serif;font-weight:600;font-size:16px;margin-top:90px}
.stars{color:#e7b52c;font-size:10px;letter-spacing:1px;margin-top:4px}
.bubble p{font-size:13.5px;line-height:26px;color:var(--muted);width:270px;margin:8px auto 0}
/* thank you */
.contact{display:flex;align-items:center;gap:20px;font-size:16px;line-height:26px}
.contact .ico{width:52px;height:52px;border-radius:50%;background:var(--deep);display:flex;align-items:center;justify-content:center;flex:none}
</style>
</head>
<body>

<!-- Cover -->
<section class="slide s1">
  <svg class="abs" width="1112" height="625" viewBox="0 0 1112 625">
    <defs><linearGradient id="team" x1="0" y1="0" x2="1" y2="1"><stop offset="0" stop-color="#c8d4d8"/><stop offset=".5" stop-color="#4d5a62"/><stop offset="1" stop-color="#2c3338"/></linearGradient></defs>
    <path d="M424,0 C560,30 620,260 540,430 C490,540 400,625 262,625 L1112,625 L1112,0 Z" fill="var(--deep)"/>
    <path d="M596,0 L1112,0 L1112,580 L800,580 C700,580 650,490 650,380 C650,250 665,100 596,0 Z" fill="url(#team)" role="img" aria-label="Photo of a business team meeting around a table"/>
  </svg>
  <div class="abs wordmark large" style="left:34px;top:175px"><span class="dot"></span>VALOREON</div>
  <h1 class="abs title hero-title" style="left:34px;top:340px">YOU NEED VALUE.<br>WE DELIVER.</h1>
  <div class="abs date" style="left:36px;top:484px">
    <svg width="18" height="18" viewBox="0 0 18 18" fill="none" stroke="#5d6664" stroke-width="1.6"><rect x="2" y="3.5" width="14" height="12.5" rx="1.5"/><path d="M2 7.5h14M6 1.5v4M12 1.5v4"/></svg>16 August 2023
  </div>
</section>

<!-- Agenda -->
<section class="slide s2">
  <div class="abs agenda-frame"></div>
  <div class="abs agenda-photo photo" role="img" aria-label="Photo of two colleagues reviewing documents at a laptop"></div>
  <div class="abs soft-circle"></div>
  <div class="abs wordmark small corner-mark"><span class="dot"></span>VALOREON</div>
  <h2 class="abs title agenda-title">AGENDA</h2>
  <ul class="abs agenda-list">
    <li><span class="num">i</span>Introduction</li>
    <li><span class="num">ii</span>Capability Statement</li>
    <li><span class="num">iii</span>Our Services</li>
    <li><span class="num">iv</span>Core Competencies</li>
    <li><span class="num">v</span>Why Choose Us</li>
    <li><span class="num">vi</span>Thank you</li>
  </ul>
</section>

<!-- Capability statement -->
<section class="slide s3">
  <h2 class="abs title slide-title">CAPABILITY STATEMENT</h2>
  <div class="abs wordmark small corner-mark"><span class="dot"></span>VALOREON</div>
  <div class="abs body-copy cap-copy">
    <p>Lorem ipsum dolor sit amet, consectetur adipiscing elit, sed do eiusmod tempor incididunt ut labore et dolore magna aliqua. Ut enim ad minim veniam, quis nostrud exercitation ullamco laboris nisi ut aliquip ex ea commodo consequat. Duis aute irure dolor in reprehenderit in voluptate velit esse cillum dolore eu fugiat nulla pariatur. Excepteur sint occaecat cupidatat non proident, sunt in culpa qui officia deserunt mollit anim id est laborum.</p>
    <p>Labore et dolore magna aliqua. Ut enim ad minim veniam, quis nostrud exercitation ullamco laboris nisi ut aliquip ex ea commodo consequat. Duis aute irure dolor in reprehenderit in voluptate velit esse cillum dolore eu fugiat nulla pariatur.</p>
  </div>
  <div class="abs cap-frame"></div>
  <div class="abs cap-photo" role="img" aria-label="Photo of a businessman behind chess pieces on a wooden table"></div>
</section>

<!-- Services -->
<section class="slide s4">
  <h2 class="abs title slide-title">OUR SERVICES</h2>
  <div class="abs wordmark small corner-mark"><span class="dot"></span>VALOREON</div>
  <p class="abs intro">Lorem ipsum dolor sit amet, consectetur adipiscing elit, sed do eiusmod tempor incididunt ut labore et dolore magna aliqua. Ut enim ad minim veniam, quis nostrud exercitation ullamco.</p>

  <div class="abs service" style="left:33px">
    <div class="ring"><div class="core" style="background:var(--teal)">
      <svg width="50" height="50" viewBox="0 0 50 50" fill="none" stroke="#fff" stroke-width="3.5"><circle cx="24" cy="26" r="17"/><circle cx="24" cy="26" r="9"/><circle cx="24" cy="26" r="2" fill="#fff"/><path d="M24 26L40 10M35 9h6v6"/></svg>
    </div></div>
    <h3>COMMERCIAL STRATEGY</h3>
    <p>Lorem ipsum dolor sit amet, consectetur adipi scing elit, sed do eiusmod tempor in cididunt ut labore et dolore magna aliqua. Quis ipsum suspendisse ultrices gravida.</p>
  </div>
  <div class="abs service" style="left:399px">
    <div class="ring" style="background:#c7f4df"><div class="core" style="background:var(--bright)">
      <svg width="52" height="40" viewBox="0 0 52 40" fill="none" stroke="#fff" stroke-width="3.5" stroke-linejoin="round"><path d="M2 14l10-8 8 4h12l8-4 10 8-8 12-14 10-14-10z"/><path d="M20 16l8 8M24 12l10 10"/></svg>
    </div></div>
    <h3>NEGOTIATION</h3>
    <p>Lorem ipsum dolor sit amet, consectetur adipi scing elit, sed do eiusmod tempor in cididunt ut labore et dolore magna aliqua. Quis ipsum suspendisse ultrices gravida.</p>
  </div>
  <div class="abs service" style="left:763px">
    <div class="ring"><div class="core" style="background:var(--teal)">
      <svg width="50" height="50" viewBox="0 0 50 50" fill="#fff"><rect x="26" y="32" width="5" height="12"/><rect x="34" y="26" width="5" height="18"/><rect x="42" y="20" width="5" height="24"/><circle cx="14" cy="36" r="8"/><circle cx="12" cy="10" r="4"/><circle cx="38" cy="10" r="4"/><circle cx="25" cy="18" r="4"/><path d="M12 10L25 18L38 10" stroke="#fff" stroke-width="2.5" fill="none"/></svg>
    </div></div>
    <h3>BUSINESS MODELING</h3>
    <p>Lorem ipsum dolor sit amet, consectetur adipi scing elit, sed do eiusmod tempor in cididunt ut labore et dolore magna aliqua. Quis ipsum suspendisse ultrices gravida.</p>
  </div>
</section>

<!-- Testimonial -->
<section class="slide s5">
  <h2 class="abs title slide-title">TESTIMONIAL</h2>
  <div class="abs wordmark small corner-mark"><span class="dot"></span>VALOREON</div>

  <div class="abs bubble" style="left:37px;top:184px">
    <div class="avatar" style="top:-20px" role="img" aria-label="Portrait photo of a client"></div>
    <h3>ALEX MARLOW</h3><div class="stars">★★★★★</div>
    <p>Lorem ipsum dolor sit amet, con sectetur adipiscing elit, sed do smod tempor incididunt ut labore et dolore magna aliqua. Quis ipsum suspendisis.</p>
  </div>
  <div class="abs bubble" style="left:390px;top:220px">
    <div class="avatar" style="top:-20px" role="img" aria-label="Portrait photo of a client"></div>
    <h3>ALEX MARLOW</h3><div class="stars">★★★★★</div>
    <p>Lorem ipsum dolor sit amet, con sectetur adipiscing elit, sed do smod tempor incididunt ut labore et dolore magna aliqua. Quis ipsum suspendisis.</p>
  </div>
  <div class="abs bubble" style="left:745px;top:184px">
    <div class="avatar" style="top:-20px" role="img" aria-label="Portrait photo of a client"></div>
    <h3>ALEX MARLOW</h3><div class="stars">★★★★★</div>
    <p>Lorem ipsum dolor sit amet, con sectetur adipiscing elit, sed do smod tempor incididunt ut labore et dolore magna aliqua. Quis ipsum suspendisis.</p>
  </div>
</section>

<!-- Thank you -->
<section class="slide s6">
  <svg class="abs" width="1112" height="625" viewBox="0 0 1112 625">
    <defs><linearGradient id="bar" x1="0" y1="0" x2="0" y2="1"><stop offset="0" stop-color="#22ef9c"/><stop offset="1" stop-color="#0b6e5b"/></linearGradient></defs>
    <path d="M424,0 C560,30 620,260 540,430 C490,540 400,625 262,625 L1112,625 L1112,0 Z" fill="var(--deep)"/>
    <path d="M596,0 L1112,0 L1112,625 L800,625 C700,600 650,490 650,380 C650,250 665,100 596,0 Z" fill="#eef3f2"/>
    <rect x="644" y="280" width="100" height="345" fill="url(#bar)"/>
    <rect x="777" y="147" width="100" height="478" fill="url(#bar)"/>
    <rect x="909" y="32" width="100" height="593" fill="url(#bar)"/>
    <rect x="1041" y="0" width="71" height="625" fill="url(#bar)"/>
  </svg>
  <div class="abs wordmark large" style="left:34px;top:130px"><span class="dot"></span>VALOREON</div>
  <h2 class="abs title hero-title" style="left:34px;top:254px">THANK YOU.</h2>
  <div class="abs contact" style="left:34px;top:333px">
    <span class="ico"><svg width="20" height="24" viewBox="0 0 20 24" fill="#fff"><path d="M10 0a9 9 0 0 0-9 9c0 7 9 15 9 15s9-8 9-15a9 9 0 0 0-9-9zm0 12.5a3.5 3.5 0 1 1 0-7 3.5 3.5 0 0 1 0 7z"/></svg></span>
    <div>ADDRESS:<br>Valoreon, Address comes here.</div>
  </div>
  <div class="abs contact" style="left:34px;top:424px">
    <span class="ico"><svg width="20" height="20" viewBox="0 0 24 24" fill="#fff"><path d="M6.6 10.8a15 15 0 0 0 6.6 6.6l2.2-2.2c.3-.3.7-.4 1-.2 1.1.4 2.3.6 3.6.6.6 0 1 .4 1 1V20c0 .6-.4 1-1 1A17 17 0 0 1 3 4c0-.6.4-1 1-1h3.5c.6 0 1 .4 1 1 0 1.3.2 2.5.6 3.6.1.3 0 .7-.2 1z"/></svg></span>
    <div>PHONE:<br>0040700000000</div>
  </div>
  <div class="abs contact" style="left:34px;top:514px">
    <span class="ico"><svg width="20" height="16" viewBox="0 0 20 16" fill="#fff"><path d="M0 2a2 2 0 0 1 2-2h16a2 2 0 0 1 2 2v.5L10 8 0 2.5zM0 4.8l10 5.7 10-5.7V14a2 2 0 0 1-2 2H2a2 2 0 0 1-2-2z"/></svg></span>
    <div>EMAIL:<br>hello@valoreon.example</div>
  </div>
</section>

</body>
</html>
```